Private Medical Clinic needs a letterhead design

Letterhead that can be edited. Letter head is needed for printing official doctor's notes, referrals, etc in a medical clinic. The letterhead should use the attached logos

```html
<!DOCTYPE html>
<html lang="en">
<head>
<meta charset="utf-8">
<title>Stillwater Family Medicine — Letterhead</title>
<link rel="stylesheet" href="https://fonts.googleapis.com/css2?family=Crimson+Pro:wght@400&family=Open+Sans:wght@400&display=swap">
<style>
  :root {
    --backdrop: #f7f7f7;
    --paper: #ffffff;
    --paper-edge: #e4e4e4;
    --ink: #4a4a47;
    --ink-soft: #6d6d6a;
    --seed-tone: #d9d9d9;
  }
  * { margin: 0; padding: 0; box-sizing: border-box; }
  html, body {
    width: 1200px;
    height: 785px;
    overflow: hidden;
    background: var(--backdrop);
  }
  .canvas {
    position: relative;
    width: 1200px;
    height: 785px;
    display: flex;
    align-items: center;
    justify-content: center;
  }
  .letterhead {
    position: relative;
    width: 508px;
    height: 720px;
    background: var(--paper);
    border: 1px solid var(--paper-edge);
    overflow: hidden;
  }
  .seed-band {
    position: absolute;
    top: 0;
    left: 0;
    width: 100%;
    height: 120px;
    background:
      radial-gradient(ellipse 120px 60px at 62% 0%, var(--seed-tone), transparent 75%),
      radial-gradient(ellipse 140px 80px at 92% 10%, var(--seed-tone), transparent 75%),
      radial-gradient(ellipse 120px 70px at 12% 8%, #e6e6e6, transparent 75%),
      radial-gradient(ellipse 90px 50px at 40% 0%, #ebebeb, transparent 75%);
    opacity: 0.8;
  }
  .seed-corner {
    position: absolute;
    bottom: 0;
    width: 110px;
    height: 85px;
    opacity: 0.8;
  }
  .seed-corner--left {
    left: 0;
    background: radial-gradient(ellipse 100px 80px at 10% 100%, var(--seed-tone), transparent 75%);
  }
  .seed-corner--right {
    right: 0;
    background: radial-gradient(ellipse 100px 80px at 90% 100%, var(--seed-tone), transparent 75%);
  }
  .brand {
    position: absolute;
    top: 54px;
    left: 44px;
    display: flex;
    align-items: center;
    gap: 8px;
    font-family: "Crimson Pro", Georgia, serif;
    font-weight: 400;
    color: var(--ink);
  }
  .brand__dot {
    width: 10px;
    height: 10px;
    border-radius: 50%;
    background: var(--ink);
  }
  .brand__name {
    font-size: 29px;
    line-height: 1;
  }
  .brand__sub {
    display: block;
    margin-top: 5px;
    font-size: 7.5px;
    letter-spacing: 1.4px;
    text-transform: uppercase;
    padding-left: 12px;
  }
  .footer {
    position: absolute;
    left: 0;
    right: 0;
    bottom: 10px;
    text-align: center;
    color: var(--ink);
  }
  .footer__tagline {
    font-family: "Crimson Pro", Georgia, serif;
    font-size: 13px;
    letter-spacing: 1.1px;
    margin-bottom: 14px;
  }
  .footer__contact {
    font-family: "Open Sans", Arial, sans-serif;
    font-size: 4.6px;
    line-height: 1.35;
    color: var(--ink-soft);
    margin-bottom: 6px;
  }
  .footer__web {
    font-family: "Open Sans", Arial, sans-serif;
    font-size: 7px;
    letter-spacing: 0.2px;
  }
</style>
</head>
<body>
  <main class="canvas">
    <article class="letterhead">
      <div class="seed-band" role="img" aria-label="Soft grey dandelion seed illustration along the top edge"></div>
      <div class="seed-corner seed-corner--left" role="img" aria-label="Faint dandelion seed illustration in lower left corner"></div>
      <div class="seed-corner seed-corner--right" role="img" aria-label="Faint dandelion seed illustration in lower right corner"></div>

      <header class="brand">
        <span class="brand__dot"></span>
        <div>
          <span class="brand__name">Stillwater</span>
          <span class="brand__sub">Family Medicine</span>
        </div>
      </header>

      <footer class="footer">
        <p class="footer__tagline">Healing the Whole Person</p>
        <p class="footer__contact">
          Stillwater Family Medicine, LLC<br>
          Phone: 555-214-3680<br>
          Fax: 555-339-7021<br>
          info@stillwatermedicine.com
        </p>
        <p class="footer__web">www.stillwatermedicine.com</p>
      </footer>
    </article>
  </main>
</body>
</html>
```